Real estate investor, needing a business card that communicates warmth, integrity, empathy.

I have a logo that can be manipulated to align with the message - "Serving your home selling needs." Want it to stand out from typical real estate investor cards, and make distressed home sellers feel a connection with me. Should communicate warmth, integrity, empathy, and trustworthiness.

Target Market(s)

Distressed home owners who need to sell their homes, not using realtors.

Contact Information for Business Card

Glossy front and matte back, with a small box that is labelled "notes." I like darker blues and blacks together, but doesn't have to be, as long as it communicates trustworthiness, and a strong call to action.

Other font styles liked:
• see "must haves" above, but willing to review whatever comes my way.

Requirements
Must have
• The fonts on my logo are Aviano, Lusitana, and Marcellus. We don't have to use those, but I favor them.

```html
<!DOCTYPE html>
<html lang="en">
<head>
<meta charset="utf-8">
<title>Daniel Reyes – Business Card</title>
<link rel="stylesheet" href="https://fonts.googleapis.com/css2?family=Archivo:wght@800&family=Open+Sans:wght@400;600;700&display=swap">
<style>
  :root {
    --backdrop: #dedede;
    --card: #ffffff;
    --bronze: #a67849;
    --headline: #444444;
    --ink: #1a1a1a;
    --on-bronze: #ffffff;
  }
  html, body {
    margin: 0;
    padding: 0;
    width: 1200px;
    height: 800px;
    overflow: hidden;
    background: var(--backdrop);
  }
  .business-card {
    position: absolute;
    left: 40px;
    top: 80px;
    width: 1120px;
    height: 640px;
    background: var(--card);
    overflow: hidden;
    font-family: "Open Sans", Arial, sans-serif;
  }
  .bronze-band {
    position: absolute;
    inset: 0;
    width: 1120px;
    height: 640px;
  }
  .bronze-band polygon { fill: var(--bronze); }
  .tagline {
    position: absolute;
    left: 41px;
    top: 58px;
    margin: 0;
    font-family: "Archivo", "Helvetica Neue", Arial, sans-serif;
    font-weight: 800;
    font-size: 56px;
    line-height: 57px;
    letter-spacing: -0.5px;
    color: var(--headline);
    text-transform: uppercase;
  }
  .agent {
    position: absolute;
    left: 65px;
    top: 318px;
    color: var(--on-bronze);
  }
  .agent-name {
    margin: 0;
    font-size: 55px;
    line-height: 60px;
    font-weight: 400;
    letter-spacing: 0.5px;
  }
  .agent-name .first { font-weight: 700; }
  .agent-role {
    margin: 0;
    font-size: 26px;
    line-height: 28px;
    font-weight: 600;
  }
  .agent-rule {
    width: 96px;
    height: 3px;
    background: var(--on-bronze);
    margin-top: 20px;
  }
  .contact-list {
    list-style: none;
    margin: 18px 0 0;
    padding: 0;
  }
  .contact-list li {
    display: flex;
    align-items: center;
    gap: 14px;
    font-size: 26px;
    line-height: 37px;
    font-weight: 400;
  }
  .contact-list svg {
    width: 22px;
    height: 22px;
    fill: var(--on-bronze);
    flex: none;
  }
  .brand-name {
    position: absolute;
    left: 700px;
    top: 300px;
    width: 340px;
    text-align: center;
    font-family: "Open Sans", Arial, sans-serif;
    font-weight: 700;
    font-size: 40px;
    letter-spacing: 4px;
    color: var(--ink);
    text-transform: uppercase;
  }
</style>
</head>
<body>
  <div class="business-card">
    <svg class="bronze-band" viewBox="0 0 1120 640" aria-hidden="true">
      <polygon points="0,262 500,262 725,526 1120,526 1120,598 0,598"/>
    </svg>

    <h1 class="tagline">Serving<br>your home<br>selling needs.</h1>

    <div class="agent">
      <p class="agent-name"><span class="first">DANIEL</span> REYES</p>
      <p class="agent-role">Real Estate Agent</p>
      <div class="agent-rule"></div>
      <ul class="contact-list">
        <li>
          <svg viewBox="0 0 24 24" aria-hidden="true"><path d="M6.6 10.8a15.1 15.1 0 0 0 6.6 6.6l2.2-2.2c.3-.3.7-.4 1-.2 1.1.4 2.3.6 3.6.6.6 0 1 .4 1 1V20c0 .6-.4 1-1 1A17 17 0 0 1 3 4c0-.6.4-1 1-1h3.5c.6 0 1 .4 1 1 0 1.3.2 2.5.6 3.6.1.3 0 .7-.2 1z"/></svg>
          <span>+000 12345 6789</span>
        </li>
        <li>
          <svg viewBox="0 0 24 24" aria-hidden="true"><path d="M2 4h20v13H13v2h3v2H8v-2h3v-2H2zm2 2v9h16V6z"/></svg>
          <span>urwebsitename.com</span>
        </li>
        <li>
          <svg viewBox="0 0 24 24" aria-hidden="true"><path d="M12 2a7 7 0 0 0-7 7c0 5.2 7 13 7 13s7-7.8 7-13a7 7 0 0 0-7-7zm0 9.5A2.5 2.5 0 1 1 12 6.5a2.5 2.5 0 0 1 0 5z"/></svg>
          <span>Your street address here-1234</span>
        </li>
      </ul>
    </div>

    <div class="brand-name">Larkfield</div>
  </div>
</body>
</html>
```